WTF!!! We need a modern professional website for a business litigation law firm.

We need a modern, clean, professional and uncomplicated website for a new business trial and litigation law firm called "Harrowgate Trial Firm PLLC". Website must be mobile optimized for iPad and smartphone. The law firm specializes in counseling and representing large corporations, small businesses and entrepreneurs in and out of the courtroom. Lawyers in the firm serve as Florida counsel and trial counsel to organizations facing claims involving product liability, premises liability, professional liability, vehicle and transportation liability, warranty claims, construction defects and delay claims, complex business disputes, commercial litigation and bid disputes in State and Federal Courts. The website is mainly to provide information about the firm, and should include sections describing the firm, identifying the Industries Served and Areas of Practice ," a separate page identifying the "Professionals", a separate page for "Resources & Advisories," and a traveling "Connect With Us" button a site visitor can click on that will launch an email to the Firm's general email account. The website should allow us to easily modify the content on these pages, and let us add/modify links to external information sources. We will not sell anything or take payments through the website. We do need to be able to easily upload and update photographs of attorneys and add new attorneys names/email hyperlinks as the firm grows. We would like to add developments in the law or success stories easily and quickly, such as through a blog page. On the "Connect With Us" page the website should have hyperlinks to email the Firm, and there should be hyperlinks to email each professional on the "Professionals" page. The website should be viewable on mobile devices without distortion. The law firm focuses on trial work and should have some imagery associated with courtrooms, but the overall theme of the site should be modern, clean, and communicate sophistication and strength. The website should be made in Wordpress. We have uploaded logo files for Harrowgate Trial Firm.

Target Market(s)

Corporations and companies that are looking for legal representation. Other attorneys/legal industry.

Industry/Entity Type

Legal Industry

Coding

Coded - Design and coding required

Number of Pages Required

1 page

Font styles to use
Sans Serif

Requirements
Must have
• Simple, clean, sophisticated, modern website that includes the logo, watermark of logo, and the elements described above.
Nice to have
• Pictures of city scape, buildings, courtroom, team members.

```html
<!DOCTYPE html>
<html lang="en">
<head>
<meta charset="utf-8">
<title>Harrowgate Trial Firm</title>
<link rel="stylesheet" href="https://fonts.googleapis.com/css2?family=Poppins:wght@400;500;600;700;800&family=Roboto:wght@400;500;700&family=Lato:wght@400;700&family=Cormorant+Garamond:wght@500&display=swap">
<style>
:root{
  --accent:#c97a3c;
  --ink:#2b2838;
  --navy:#36324a;
  --navy-soft:#403b56;
  --muted:#5c5a66;
  --light:#f0f0f0;
  --white:#ffffff;
}
*{box-sizing:border-box;margin:0;padding:0}
html,body{width:1200px;height:4533px;overflow:hidden;background:var(--white)}
body{font-family:"Roboto",sans-serif;color:var(--ink);position:relative}
.abs{position:absolute}
.btn{position:absolute;background:var(--accent);color:var(--white);font-family:"Poppins",sans-serif;font-size:13px;display:flex;align-items:center;justify-content:center;text-transform:uppercase;letter-spacing:.3px}

.admin-bar{top:0;left:0;width:1200px;height:30px;background:#1d2327;color:#e6e6e6;font-size:11px;display:flex;align-items:center;padding:0 12px;gap:18px}
.admin-bar .right{margin-left:auto}
.info-bar{top:30px;left:0;width:1200px;height:51px;background:var(--light);font-family:"Poppins",sans-serif;font-size:13px;display:flex;align-items:center;padding:0 28px}
.info-bar .socials{margin-left:auto;display:flex;gap:34px;margin-right:18px}
.info-bar .socials span{width:12px;height:12px;border-radius:50%;background:var(--ink)}
.site-header{top:81px;left:0;width:1200px;height:97px;background:var(--white)}
.brand{left:37px;top:34px;font-family:"Poppins",sans-serif;font-weight:700;font-size:22px;color:var(--ink);display:flex;align-items:center;gap:10px}
.brand i{width:16px;height:16px;background:var(--ink);display:block}
.nav{right:204px;top:36px;display:flex;gap:42px;font-family:"Poppins",sans-serif;font-size:14px;color:var(--ink)}
.nav .active{color:#8a8a8a}
.hero{top:178px;left:0;width:1200px;height:927px;background:linear-gradient(100deg,#1f1f1e 0%,#2d2f2b 40%,#55564f 65%,#7a7a72 100%)}
.hero-eyebrow{left:37px;top:186px;font-family:"Lato",sans-serif;font-size:25px;letter-spacing:1.5px;color:var(--accent)}
.hero-title{left:37px;top:245px;font-family:"Poppins",sans-serif;font-weight:800;font-size:88px;line-height:90px;color:var(--white);letter-spacing:-1px}
.hero-text{left:37px;top:552px;width:490px;font-family:"Lato",sans-serif;font-size:15px;line-height:23px;color:#e8e8e8}
.industries{top:1105px;left:0;width:1200px;height:275px;background:var(--navy)}
.industry{position:absolute;top:60px;width:192px;text-align:center;color:var(--white);font-size:21px;line-height:26px}
.industry svg{display:block;margin:0 auto 18px}
.about-photo{left:37px;top:1670px;width:496px;height:468px;border-radius:6px;background:linear-gradient(135deg,#e6e4e0 0%,#bdb6ab 45%,#5a4a3c 100%)}
.about-eyebrow{left:628px;top:1668px;font-family:"Poppins",sans-serif;font-weight:500;font-size:28px;color:var(--accent)}
.about-title{left:628px;top:1716px;font-family:"Poppins",sans-serif;font-weight:600;font-size:33px;line-height:43px;color:var(--ink)}
.about-text{left:628px;width:525px;font-family:"Poppins",sans-serif;font-size:11px;line-height:21px;color:var(--muted)}
.eyebrow{font-family:"Roboto",sans-serif;font-weight:500;font-size:17px;letter-spacing:1.5px;color:var(--accent);text-transform:uppercase}
.col-title{font-family:"Roboto",sans-serif;font-weight:500;font-size:33px;line-height:35px;color:var(--ink)}
.col-text{font-family:"Roboto",sans-serif;font-size:14px;line-height:24px;color:var(--muted)}
.feature-title{font-family:"Roboto",sans-serif;font-weight:500;font-size:24px;color:var(--ink)}
.icon-box{width:71px;height:71px;background:var(--accent);border-radius:3px;display:flex;align-items:center;justify-content:center}
.mission-photo{left:398px;top:2270px;width:330px;height:466px;background:linear-gradient(180deg,#ffffff 0%,#ffffff 30%,#d3d3d3 30%,#c4c4c4 100%)}
.help{top:2894px;left:0;width:1200px;height:540px;background:var(--navy);overflow:hidden}
.help-title{top:3141px;left:0;width:1200px;text-align:center;font-family:"Roboto",sans-serif;font-weight:500;font-size:43px;line-height:62px;color:var(--white)}
.card{position:absolute;top:3343px;width:354px;height:287px;border-radius:6px;overflow:hidden}
.card h3{position:absolute;left:37px;top:203px;font-family:"Poppins",sans-serif;font-weight:600;font-size:23px;color:var(--white)}
.card p{position:absolute;left:37px;top:251px;font-family:"Roboto",sans-serif;font-size:13px;color:var(--white)}
.arrow{position:absolute;top:3683px;width:44px;height:47px;background:var(--navy);border-radius:3px;display:flex;align-items:center;justify-content:center}
.results-title{top:3950px;left:0;width:1200px;text-align:center;font-family:"Roboto",sans-serif;font-weight:500;font-size:43px;line-height:62px;color:var(--ink)}
.stat{position:absolute;top:4140px;width:300px;text-align:center}
.stat b{display:block;font-family:"Cormorant Garamond",serif;font-weight:500;font-size:86px;line-height:90px;color:var(--accent)}
.stat span{display:block;font-family:"Roboto",sans-serif;font-size:17px;color:var(--ink);margin-top:2px}
</style>
</head>
<body>

<div class="abs admin-bar">
  <span>Harrowgate Firm</span><span>Customize</span><span>2</span><span>0</span><span>+ New</span><span>Edit Page</span><span>Edit with Layoutly</span><span>Notes</span><span>Duplicate Post</span>
  <span class="right">Howdy, admin</span>
</div>

<div class="abs info-bar">
  <span>◷&nbsp;&nbsp;Mon - Fri 10:00-18:00</span>
  <div class="socials"><span></span><span></span><span></span></div>
</div>

<header class="abs site-header">
  <div class="abs brand"><i></i>HARROWGATE</div>
  <nav class="abs nav">
    <span class="active">Home</span><span>Practice Areas</span><span>Attorney</span><span>Advisories</span><span>Blog</span>
  </nav>
  <div class="btn" style="left:1013px;top:18px;width:148px;height:54px">Contact Us</div>
</header>

<section class="abs hero" role="img" aria-label="Lawyer in white shirt and tie working on a laptop outdoors">
  <div class="abs hero-eyebrow">COUNSEL LAW FIRM</div>
  <h1 class="abs hero-title">Best Law<br>Firm Since<br>2015</h1>
  <p class="abs hero-text">At Harrowgate Trial Firm, we've been providing trusted counsel to businesses and individuals for over 10 years. Our focus on strategic legal solutions ensures that we handle even the most complex matters with precision and dedication.</p>
  <div class="btn" style="left:37px;top:686px;width:185px;height:53px">Legal Services</div>
</section>

<section class="abs industries">
  <div class="industry" style="left:23px"><svg width="70" height="74" viewBox="0 0 70 74" fill="none" stroke="#fff" stroke-width="2"><rect x="25" y="12" width="14" height="28" transform="rotate(45 32 26)"/><line x1="33" y1="34" x2="13" y2="54"/><rect x="33" y="56" width="28" height="6"/></svg>Manufacturing</div>
  <div class="industry" style="left:215px"><svg width="70" height="74" viewBox="0 0 70 74" fill="none" stroke="#fff" stroke-width="2"><path d="M9 30 L35 6 L61 30 V70 H9 Z"/><line x1="25" y1="34" x2="45" y2="54"/><rect x="33" y="24" width="10" height="20" transform="rotate(45 38 34)"/></svg>Construction &amp;<br>Real Estate</div>
  <div class="industry" style="left:407px"><svg width="70" height="74" viewBox="0 0 70 74" fill="none" stroke="#fff" stroke-width="2"><rect x="6" y="28" width="40" height="22"/><path d="M46 34 H58 L64 42 V50 H46"/><circle cx="18" cy="54" r="5"/><circle cx="54" cy="54" r="5"/></svg>Transportation</div>
  <div class="industry" style="left:599px"><svg width="70" height="74" viewBox="0 0 70 74" fill="none" stroke="#fff" stroke-width="2"><path d="M28 10 L50 18 V40 C50 56 40 64 28 70 C16 64 6 56 6 40 V18 Z"/><circle cx="48" cy="14" r="6"/><path d="M40 70 V30 H58 V70"/></svg>Professional<br>Liability</div>
  <div class="industry" style="left:791px"><svg width="70" height="74" viewBox="0 0 70 74" fill="none" stroke="#fff" stroke-width="2"><rect x="14" y="8" width="40" height="56" rx="3"/><line x1="22" y1="22" x2="46" y2="22"/><line x1="22" y1="32" x2="46" y2="32"/><circle cx="34" cy="48" r="8"/></svg>Retail</div>
  <div class="industry" style="left:983px"><svg width="70" height="74" viewBox="0 0 70 74" fill="none" stroke="#fff" stroke-width="2"><rect x="10" y="8" width="50" height="40" rx="3"/><line x1="35" y1="48" x2="35" y2="62"/><line x1="22" y1="64" x2="48" y2="64"/><line x1="35" y1="16" x2="35" y2="40"/><line x1="22" y1="22" x2="48" y2="22"/><path d="M18 34 L22 22 L26 34 Z M44 34 L48 22 L52 34 Z"/></svg>Technology &amp;<br>Startups</div>
</section>

<div class="abs about-photo" role="img" aria-label="Lawyer in suit signing documents at a wooden desk"></div>
<div class="abs about-eyebrow">About us</div>
<h2 class="abs about-title">Welcome To The Counsel<br>Law Firm</h2>
<p class="abs about-text" style="top:1822px">wonderful serenity has taken possession of my entire soul, like these sweet mornings of spring which I enjoy with my whole heart.A wonderful serenity has taken possession of my entire soul, like these sweet mornings of spring which I enjoy with my whole heart.</p>
<p class="abs about-text" style="top:1917px">wonderful serenity has taken possession of my entire soul, like these sweet mornings of spring which I enjoy with my whole heart</p>
<div class="btn" style="left:628px;top:1993px;width:151px;height:44px">Read More</div>

<div class="abs eyebrow" style="left:42px;top:2268px">Our Mission</div>
<h2 class="abs col-title" style="left:42px;top:2303px">We’re Recognized In<br>All Legal Practises</h2>
<p class="abs col-text" style="left:42px;top:2394px;width:330px">Excellence Across All Legal Practices. Trusted. Proven Respected a Legacy of Success in Every Area of Law We Practice.</p>
<div class="abs icon-box" style="left:42px;top:2523px"><svg width="34" height="34" viewBox="0 0 34 34" fill="none" stroke="#fff" stroke-width="2"><path d="M17 3 L30 8 V18 C30 26 24 30 17 32 C10 30 4 26 4 18 V8 Z"/><circle cx="17" cy="17" r="6"/></svg></div>
<h3 class="abs feature-title" style="left:42px;top:2612px">Trusted Law Firm</h3>
<p class="abs col-text" style="left:42px;top:2658px;width:330px">Your Trusted Legal Partner in Every Challenge. Trust integrity, Excellence in Litigation and Business Law</p>

<div class="abs mission-photo" role="img" aria-label="Smiling lawyer in dark suit and blue shirt standing"></div>

<div class="abs eyebrow" style="left:827px;top:2268px">Why Choose Us</div>
<h2 class="abs col-title" style="left:827px;top:2303px">We Solve Complex<br>Legal Issues</h2>
<p class="abs col-text" style="left:827px;top:2394px;width:340px">Experience. Strategy. Solutions for Complex Legal Matters turning Legal Challenges into Legal Victories</p>
<div class="abs icon-box" style="left:827px;top:2523px"><svg width="34" height="34" viewBox="0 0 34 34" fill="none" stroke="#fff" stroke-width="2"><rect x="4" y="10" width="26" height="18" rx="2"/><path d="M12 10 V6 H22 V10"/><line x1="4" y1="18" x2="30" y2="18"/></svg></div>
<h3 class="abs feature-title" style="left:827px;top:2612px">Find Best Lawyers</h3>
<p class="abs col-text" style="left:827px;top:2658px;width:340px">Find the Right Lawyers. Get the Best Results. Elite advocacy trusted Counsel and Outstanding Results</p>

<section class="abs help">
  <svg class="abs" style="left:0;top:0" width="1200" height="540" viewBox="0 0 1200 540"><path d="M0 60 C120 160 160 330 380 540 L0 540 Z" fill="var(--navy-soft)"/></svg>
</section>
<div class="abs eyebrow" style="left:0;top:3085px;width:1200px;text-align:center">How We Can Help</div>
<h2 class="abs help-title">Meeting the needs of our clients<br>since 2015.</h2>

<div class="card" style="left:39px;background:linear-gradient(135deg,#3b5f86 0%,#6e8fb0 60%,#d8dde2 100%)" role="img" aria-label="Businessman in blue shirt thinking at his desk"><h3>Corporate Matter</h3><p>Legal Excellence in Corporate Affairs</p></div>
<div class="card" style="left:422px;background:linear-gradient(135deg,#3a2a4a 0%,#6a4a3a 50%,#1e1a22 100%)" role="img" aria-label="Judge's gavel and scales in a law library"><h3>Marriage Contract</h3><p>Secure &amp; Fair Marriage Contracts</p></div>
<div class="card" style="left:809px;background:linear-gradient(135deg,#8a8e8c 0%,#c9c6c0 55%,#e8e6e2 100%)" role="img" aria-label="Woman reviewing business documents"><h3>Business Planning</h3><p>Strategic Legal Plans for Business Success</p></div>

<div class="arrow" style="left:549px"><svg width="14" height="14" viewBox="0 0 14 14" fill="none" stroke="#fff" stroke-width="2"><path d="M9 2 L4 7 L9 12"/></svg></div>
<div class="arrow" style="left:605px"><svg width="14" height="14" viewBox="0 0 14 14" fill="none" stroke="#fff" stroke-width="2"><path d="M5 2 L10 7 L5 12"/></svg></div>

<div class="abs eyebrow" style="left:0;top:3901px;width:1200px;text-align:center">Our Results</div>
<h2 class="abs results-title">Our Firm Is One Of The Most<br>Successful Law Firms</h2>
<div class="stat" style="left:93px"><b>88%</b><span>Cases Solved</span></div>
<div class="stat" style="left:450px"><b>6k</b><span>Happy Clients</span></div>
<div class="stat" style="left:805px"><b>96%</b><span>Successful Tasks</span></div>
<div class="btn" style="left:530px;top:4307px;width:140px;height:44px">About Us</div>

</body>
</html>
```